Business Card for plorvaTEC

Create a Business Card with an existing logo for plorvaTEC AG. We are a Information Technology company that does consulting and developing SW to automate business processes. The main colors are given from the logo.

Industry/Entity Type

Business

Requirements
Nice to have
• we use a a font style Century Gothic in our documents

```html
<!DOCTYPE html>
<html lang="en">
<head>
<meta charset="utf-8">
<title>plorvaTEC AG – Business Card</title>
<link href="https://fonts.googleapis.com/css2?family=Didact+Gothic&family=Cinzel:wght@400;600&display=swap" rel="stylesheet">
<style>
  :root {
    --bg: #e4e6e8;
    --card: #ffffff;
    --ink: #4a4d50;
    --ink-soft: #6b6f73;
    --brand-blue: #2a6db5;
    --brand-blue-deep: #1f4f95;
    --brand-green: #3a9b35;
    --icon: #3a7cc0;
  }
  * { box-sizing: border-box; margin: 0; padding: 0; }
  html, body { width: 1200px; height: 900px; overflow: hidden; }
  body {
    background: var(--bg);
    font-family: "Didact Gothic", "Century Gothic", sans-serif;
    color: var(--ink);
    display: flex;
    flex-direction: column;
    align-items: center;
    justify-content: center;
    gap: 40px;
  }
  .card {
    position: relative;
    width: 640px;
    height: 372px;
    background: var(--card);
    box-shadow: 0 6px 22px rgba(0,0,0,0.12);
    overflow: hidden;
  }
  .card-art { position: absolute; inset: 0; width: 100%; height: 100%; }

  /* Company name */
  .brand {
    position: absolute; left: 44px; top: 40px;
    display: flex; align-items: center; gap: 12px;
  }
  .brand-dot {
    width: 14px; height: 14px; border-radius: 50%;
    background: var(--brand-blue);
  }
  .brand-name { font-size: 30px; color: var(--brand-blue); letter-spacing: 1px; line-height: 1; }

  .contact-list {
    position: absolute; left: 44px; top: 112px;
    list-style: none; font-size: 13px; letter-spacing: 1.2px; line-height: 19px;
  }
  .contact-list li { display: flex; align-items: center; gap: 9px; }
  .contact-icon { width: 11px; height: 11px; flex: none; }
  .contact-list .no-icon { padding-left: 20px; }

  .person {
    position: absolute; right: 64px; top: 178px; text-align: right;
    font-family: "Cinzel", serif;
  }
  .person-name { font-size: 17px; letter-spacing: 4px; color: var(--ink); }
  .person-role { font-size: 15px; letter-spacing: 3px; color: var(--brand-green); font-weight: 600; }

  /* Back */
  .back-brand { left: 44px; top: 56px; }
  .website {
    position: absolute; right: 90px; top: 186px;
    font-size: 15px; letter-spacing: 3px; color: var(--brand-green);
  }
</style>
</head>
<body>

  <section class="card card-front" aria-label="Business card front">
    <svg class="card-art" viewBox="0 0 640 372" preserveAspectRatio="none" aria-hidden="true">
      <defs>
        <linearGradient id="swoosh-blue" x1="0" y1="0" x2="1" y2="1">
          <stop offset="0" stop-color="#3b86cc"/>
          <stop offset="1" stop-color="#1f4f95"/>
        </linearGradient>
      </defs>
      <path d="M0 205 C 150 250, 290 300, 400 305 C 500 308, 580 290, 640 270 L640 372 L0 372 Z" fill="#3a9b35"/>
      <path d="M0 218 C 150 262, 290 310, 400 314 C 500 318, 580 302, 640 284 L640 372 L0 372 Z" fill="url(#swoosh-blue)"/>
    </svg>

    <div class="brand">
      <span class="brand-dot"></span>
      <span class="brand-name">plorvaTEC</span>
    </div>

    <ul class="contact-list">
      <li class="no-icon">Sorvenweg 12, 4810 Tallberg, Switzerland</li>
      <li>
        <svg class="contact-icon" viewBox="0 0 12 12"><path d="M2 1h2.5l1 3-1.5 1a7 7 0 0 0 3 3l1-1.5 3 1V11a1 1 0 0 1-1 1A10 10 0 0 1 1 2a1 1 0 0 1 1-1z" fill="var(--icon)"/></svg>
        +41 52 318 40 66
      </li>
      <li>
        <svg class="contact-icon" viewBox="0 0 12 12"><rect x="3" y="0.5" width="6" height="11" rx="1" fill="none" stroke="var(--icon)" stroke-width="1.3"/><circle cx="6" cy="9.5" r="0.8" fill="var(--icon)"/></svg>
        +41 78 204 57 19
      </li>
      <li>
        <svg class="contact-icon" viewBox="0 0 12 12"><rect x="0.7" y="2.2" width="10.6" height="7.6" rx="1" fill="none" stroke="var(--icon)" stroke-width="1.2"/><path d="M1 3l5 3.6L11 3" fill="none" stroke="var(--icon)" stroke-width="1.2"/></svg>
        lukas.brenner@plorvatec.ch
      </li>
      <li class="no-icon">www.plorvatec.ch</li>
    </ul>

    <div class="person">
      <p class="person-name">LUKAS BRENNER</p>
      <p class="person-role">CEO</p>
    </div>
  </section>

  <section class="card card-back" aria-label="Business card back">
    <div class="brand back-brand">
      <span class="brand-dot"></span>
      <span class="brand-name">plorvaTEC</span>
    </div>
    <p class="website">www.plorvatec.ch</p>
  </section>

</body>
</html>
```